Wordpress Design For Financial Investment Company

//** NEW WIREFRAME ADDED TO HELP WITH LAYOUT ISSUES. PLEASE REFER TO WIREFRAME IN ATTACHED FILES. NO DESIGN WILL BE CONSIDERED IF IT DOES NOT FOLLOW THE WIREFRAME. **//
//** PLEASE READ THE ENTIRE BRIEF INCLUDING ALL UPDATES TO THE BRIEF. THE CLIENT IS VERY SPECIFIC ABOUT WHAT THEY WANT AND I'VE COVERED SEVERAL THINGS IN THE UPDATES. THERE IS ALSO A VIDEO UPDATE THAT HAS SOME VALUABLE INFORMATION IN IT FOR THIS CONTEST. **//
The client is an investment advisor who needs a new website designed. The current site is http://www.velmorfield.net.
The client wants the site to be green to match the attached logo.
The home page should have relevant images in the rotator. No people hugging! This is a financial investment site, not a family counseling site.
Also, the client wants 4 buttons on the home page to highlight the 4 main areas they focus on:
Investment Advice and Education
General Financial Planning
Retirement Planning
401K Planning
The top right area of the site needs to have their phone number, a call to action, and 2 buttons.
Their phone number is 303-418-7639
The call to action should say something like "Call for a free consultation!"
The buttons need to say:
Login To Your Bluvexa Account
Login To Your Quillbrook Account
The final design should communicate professionalism, financial safety and growth.
Main navigation should be:
Home
About Us
Associates
Services
Contact
Mission Statement (Could also be "Our Mission")
This is a site that the client likes: http://www.pwkinvestmentconsulting.com/
Updates
The designs should not have:
Newsletter content. A newsletter sign up is fine
Learning Center
Calculators
Stock prices/tickers
The design should have a contact form on the page.
I have talked to my client and have some updates. I did a video update because I thought it would be easier to show what I'm trying to get across.
Reason: I am going to be extending the contest a few more days. I'm still not getting quite what I want and very few people are even trying to follow the creative brief and the updates to it.
PLEASE read the entire brief and the updates. There is also a video I made that explains everything. I've also attached a wireframe.
Thanks!
Target Market(s)
People looking for a high-end financial investment company.
Industry/Entity Type
Investment
Requirements
Must have
- !!FOLLOW THE WIREFRAME FOR LAYOUT!!
!!THEIR LOGO!!
4 buttons to highlight their main practice areas
Phone number in the top right
"Free Consultation" call to action
2 Login buttons in the top right
A contact form on the page.
Should not have
- The designs should not have:
Learning Center
Calculators
Stock prices/tickers

```html
<!DOCTYPE html>
<html lang="en">
<head>
<meta charset="utf-8">
<title>Velmorfield Financial</title>
<link href="https://fonts.googleapis.com/css2?family=Arimo:wght@400;700&display=swap" rel="stylesheet">
<style>
:root{
  --green:#3f7d5e;
  --green-dark:#2b5d44;
  --green-light:#5a9a78;
  --orange:#f68b1f;
  --orange-dark:#e06f0c;
  --ink:#333;
  --muted:#555;
  --grey-band:#e6e6e6;
  --footer:#1f1f1f;
  --white:#fff;
}
*{box-sizing:border-box;margin:0;padding:0}
html,body{width:1050px;height:1200px;overflow:hidden}
body{position:relative;background:var(--white);font-family:"Arimo",Arial,sans-serif;color:var(--ink);font-size:11px}
.abs{position:absolute}
.top-strip{left:0;top:0;width:1050px;height:20px;background:linear-gradient(#4a4a4a,#2e2e2e)}
.top-strip::after{content:"";position:absolute;left:540px;top:8px;width:510px;height:12px;background:var(--white);border-radius:12px 0 0 0}
.login{top:5px;height:19px;width:151px;background:linear-gradient(var(--orange),var(--orange-dark));color:#fff;font-size:10px;text-align:center;line-height:19px;border-radius:0 0 4px 4px}
.brand{left:155px;top:42px;width:381px;height:85px}
.brand-name{position:absolute;left:0;top:22px;width:381px;text-align:center;font-size:28px;font-weight:700;color:var(--green-dark);letter-spacing:1px}
.brand-tag{position:absolute;left:0;top:72px;width:381px;text-align:center;font-size:8px;color:var(--muted)}
.ask{left:682px;top:37px;width:169px;height:36px}
.ask-title{position:absolute;left:8px;top:2px;color:#fff;font-weight:700;font-size:16px}
.ask-sub{position:absolute;left:8px;top:20px;color:#fff;font-size:11px}
.phone{left:682px;top:82px;font-size:24px;font-weight:700;color:#222}
.contact-lines{left:684px;top:108px;font-size:11.5px;line-height:16px;color:#222}
.nav{left:0;top:141px;width:1050px;height:40px;background:linear-gradient(var(--green-light),var(--green-dark))}
.nav ul{position:absolute;left:155px;top:0;display:flex;list-style:none;border-left:1px solid #2a5540}
.nav li{color:#fff;font-size:12.5px;line-height:40px;padding:0 14px;border-right:1px solid #2a5540}
.search{left:687px;top:150px;width:146px;height:24px;background:#fff;border-radius:3px;font-size:10px;line-height:24px;padding-left:8px;color:#333}
.search svg{position:absolute;right:5px;top:3px}
.hero-bg{left:0;top:181px;width:1050px;height:320px;background:linear-gradient(90deg,var(--green-dark),var(--green) 15%,var(--green) 85%,var(--green-dark))}
.hero{left:141px;top:181px;width:769px;height:320px;background:#fff}
.hero-frame{left:152px;top:188px;width:748px;height:288px;background:#fff;border:1px solid #d8d8d8;border-radius:6px;box-shadow:0 10px 14px rgba(0,0,0,.12)}
.hero-photo{left:154px;top:191px;width:490px;height:282px;background:linear-gradient(120deg,#f1e3c2,#e7b98c 45%,#c8d9a0);border-radius:4px 0 0 4px}
.hero-stat{left:154px;top:388px;width:490px;height:60px;background:rgba(110,110,110,.55);color:#fff;font-size:16px;padding-left:10px;line-height:60px}
.hero-stat b{font-size:32px;vertical-align:-3px}
.hero-title{left:650px;top:218px;width:250px;text-align:center;color:var(--green-dark);font-size:22px;font-weight:700;line-height:27px}
.hero-copy{left:656px;top:289px;width:212px;font-size:11.5px;line-height:14.5px;color:#222}
.btn{background:linear-gradient(#fca13c,var(--orange-dark));color:#fff;text-align:center;border-radius:3px}
.hero-btn{left:700px;top:401px;width:134px;height:33px;line-height:33px;font-size:13px;font-weight:700;color:#7a3a00;border-radius:6px}
.arrow{width:32px;height:32px;border-radius:50%;background:#5a3a22;border:2px solid #fff}
.dots{left:505px;top:486px;display:flex;gap:3px}
.dots i{width:7px;height:7px;border-radius:50%;background:#bbb}
.dots i:first-child{background:var(--orange)}
.band{left:0;top:501px;width:1050px;height:141px;background:var(--grey-band)}
.welcome-h{left:159px;top:510px;font-size:19px;color:#333}
.welcome-p{left:159px;top:550px;width:470px;font-size:10px;line-height:13.5px;color:#222}
.more{height:17px;width:56px;line-height:17px;font-size:9.5px}
.news{left:663px;top:514px;width:237px;height:114px;background:var(--green);border-radius:3px}
.news-h{position:absolute;left:10px;top:8px;width:170px;height:22px;background:var(--green-light);color:#fff;font-size:16px;line-height:22px;padding-left:4px}
.news-p{position:absolute;left:18px;top:40px;color:#fff;font-size:10.5px;line-height:13px}
.news-in{position:absolute;left:12px;top:76px;width:160px;height:22px;background:#fff;font-size:10.5px;line-height:22px;padding-left:8px}
.news-btn{position:absolute;left:170px;top:76px;width:61px;height:22px;line-height:22px;font-weight:700;font-size:11px}
.card{top:665px;width:183px;height:168px;border:1px solid #d4d4d4;border-radius:3px;background:linear-gradient(#fff 60%,#ebebeb);box-shadow:0 10px 10px -6px rgba(0,0,0,.2)}
.card h3{font-weight:400;font-size:12.5px;color:#444;text-align:center;margin-top:16px;white-space:nowrap}
.card-img{position:absolute;left:10px;top:46px;width:56px;height:58px;border:1px solid #ccc}
.card p{position:absolute;left:75px;top:40px;width:100px;font-size:9.3px;line-height:11.3px;color:#222}
.card .more{position:absolute;left:104px;top:138px}
.about{left:148px;top:861px;width:494px;height:152px;border:1px solid #d4d4d4;border-radius:3px}
.about h2{position:absolute;left:12px;top:8px;font-weight:400;font-size:15px;color:#333}
.about-img{position:absolute;left:12px;top:38px;width:144px;height:94px}
.about p{position:absolute;left:176px;top:40px;width:300px;font-size:10px;line-height:13.5px;color:#222}
.about .more{position:absolute;left:406px;top:122px}
.quote-h{left:158px;top:1028px;font-size:12.5px;color:#444}
.quote-box{left:148px;top:1054px;width:494px;height:54px;background:#e8e8e8;border-radius:3px}
.quote-box p{position:absolute;left:48px;top:10px;width:420px;font-size:10px;line-height:13px;color:#333}
.quote-box span{position:absolute;right:52px;top:36px;font-size:10px;color:#333}
.qc{left:663px;top:861px;width:237px;height:254px;background:#f0f0f0;border:1px solid #d8d8d8;border-radius:3px}
.qc-head{position:absolute;left:-1px;top:-1px;width:237px;height:34px;background:var(--green);border-radius:3px 3px 0 0}
.qc-head b{position:absolute;left:10px;top:6px;width:170px;height:22px;background:var(--green-light);color:#fff;font-size:15px;line-height:22px;padding-left:4px}
.qc label{position:absolute;left:12px;font-size:10.5px;color:#333}
.qc .field{position:absolute;left:66px;width:156px;height:24px;background:#fff;border:1px solid #bbb}
.qc-btn{position:absolute;left:167px;top:226px;width:56px;height:19px;line-height:19px;font-size:10.5px;font-weight:700}
.footer{left:0;top:1132px;width:1050px;height:68px;background:var(--footer);color:#fff}
.footer-links{position:absolute;top:8px;width:1050px;text-align:center;font-size:9.5px}
.follow{position:absolute;left:436px;top:28px;font-size:10.5px;display:flex;gap:3px;align-items:center}
.follow i{width:15px;height:15px;background:#5b7fb4;border-radius:2px;display:inline-block}
.follow i:last-child{background:var(--orange)}
.copy{position:absolute;top:50px;width:1050px;text-align:center;font-size:9.5px}
</style>
</head>
<body>
<div class="abs top-strip"></div>
<div class="abs login" style="left:581px">Login to your Bluvexa account</div>
<div class="abs login" style="left:744px">Login to your Quillbrook account</div>

<div class="abs brand">
  <div class="brand-name">VELMORFIELD FINANCIAL</div>
  <div class="brand-tag">"Steady guidance for every stage of life."</div>
</div>

<div class="abs ask">
  <svg width="169" height="36" viewBox="0 0 169 36"><path d="M0 3 Q0 0 3 0 H166 Q169 0 168 3 L160 33 Q159 36 156 36 H3 Q0 36 0 33Z" fill="#f68b1f"/><path d="M5 19 H80 L68 28 L70 21 H5Z" fill="#e06f0c"/></svg>
  <div class="ask-title">Any questions?</div>
  <div class="ask-sub">Call Us &nbsp; :</div>
</div>
<div class="abs phone">303 - 418 - 7639</div>
<div class="abs contact-lines">Fax &nbsp;&nbsp;&nbsp;&nbsp;&nbsp;: 303 - 418 - 7640<br>Email &nbsp;: info@velmorfield.com</div>

<nav class="abs nav"><ul><li>Home</li><li>About Us</li><li>Associates</li><li>Services</li><li>Contact</li><li>Our Mission</li></ul></nav>
<div class="abs search">Site Search
  <svg width="18" height="18" viewBox="0 0 18 18"><circle cx="7" cy="7" r="5" fill="none" stroke="#222" stroke-width="2"/><path d="M11 11 L16 16" stroke="#222" stroke-width="3"/></svg>
</div>

<div class="abs hero-bg"></div>
<div class="abs hero"></div>
<div class="abs hero-frame"></div>
<div class="abs hero-photo" role="img" aria-label="Photo of a smiling retired couple"></div>
<div class="abs hero-stat"><b>50%</b> of retirees left the workforce ealier than planned.</div>
<div class="abs hero-title">Get your question answered!</div>
<div class="abs hero-copy">For a free phone consultation, please Click Here. let us know the best dates and times you are available and leave your phone number. If you prefer to contact us, please let us know the date you would like to call.</div>
<div class="abs btn hero-btn">Free Consultation</div>
<div class="abs arrow" style="left:144px;top:316px"><svg width="28" height="28" viewBox="0 0 28 28"><path d="M16 8 L10 14 L16 20" stroke="#fff" stroke-width="3" fill="none"/></svg></div>
<div class="abs arrow" style="left:874px;top:316px"><svg width="28" height="28" viewBox="0 0 28 28"><path d="M12 8 L18 14 L12 20" stroke="#fff" stroke-width="3" fill="none"/></svg></div>
<div class="abs dots"><i></i><i></i><i></i><i></i></div>

<div class="abs band"></div>
<div class="abs welcome-h">Welcome!</div>
<div class="abs welcome-p">Lorem ipsum dolor sit amet, consecteteur adipiscing elit. set diem nonumy nibh euismod tincidunt ut laoreet dolor magna aliquam erat volutpat. ut wisi enim ad minim veniam. Nemo enim ipsam voluptatem quia voluptas sit aspermatur aut odit aut fugit, set quia consequuntur....</div>
<div class="abs btn more" style="left:571px;top:603px">Read more</div>
<div class="abs news">
  <div class="news-h">Newsletter Sign Up</div>
  <div class="news-p">Receive update news<br>from us weekly</div>
  <div class="news-in">E-mail Address</div>
  <div class="btn news-btn">SUBMIT</div>
</div>

<div class="abs card" style="left:148px"><h3>Investment Advice &amp; Education</h3><div class="card-img" role="img" aria-label="Photo of advisors meeting at a desk" style="background:linear-gradient(#dfe6ec,#9aa8b4)"></div><p>Lorem ipsum dolor sit amet, consecteteur adipiscing elit. set diem nonumy nibh eus-mod tincidunt ut laoreet dolor magna aliquam erat volutpat. ut wisl enim ad minimveniam</p><div class="btn more">Read more</div></div>
<div class="abs card" style="left:339px"><h3>General financial Planning</h3><div class="card-img" role="img" aria-label="Photo of a couple planning finances" style="background:linear-gradient(#f1e6d4,#b99873)"></div><p>Lorem ipsum dolor sit amet, consecteteur adipiscing elit. set diem nonumy nibh eus-mod tincidunt ut laoreet dolor magna aliquam erat volutpat. ut wisl enim ad minimveniam</p><div class="btn more">Read more</div></div>
<div class="abs card" style="left:529px"><h3>Retirement Planning</h3><div class="card-img" role="img" aria-label="Photo of a retired couple" style="background:linear-gradient(#dde7f0,#a9b6c2)"></div><p>Lorem ipsum dolor sit amet, consecteteur adipiscing elit. set diem nonumy nibh eus-mod tincidunt ut laoreet dolor magna aliquam erat volutpat. ut wisl enim ad minimveniam</p><div class="btn more">Read more</div></div>
<div class="abs card" style="left:720px"><h3>401K Planning</h3><div class="card-img" role="img" aria-label="Photo of banknotes and coins" style="background:linear-gradient(#f2f4ee,#a5bf9a)"></div><p>Lorem ipsum dolor sit amet, consecteteur adipiscing elit. set diem nonumy nibh eus-mod tincidunt ut laoreet dolor magna aliquam erat volutpat. ut wisl enim ad minimveniam</p><div class="btn more">Read more</div></div>

<div class="abs about">
  <h2>About Us</h2>
  <div class="about-img" role="img" aria-label="Photo of the advisory team in business suits" style="background:linear-gradient(#eceff2,#4d545c)"></div>
  <p>Lorem ipsum dolor sit amet, consectetuer adipiscing elit. set diem nonumy nibh euismod tincidunt ut laoreet dolor magna aliquam erat volutpat. Ut wisl enim veniam.<br>At vero eos et accusamus et justoodio dignissimos ducimus qui blanditis praesentium voluptatum deleniti atque corrupti quos dolores etquas...</p>
  <div class="btn more">Read more</div>
</div>
<div class="abs quote-h">What Our Client's Says About Us</div>
<svg class="abs" style="left:610px;top:1030px" width="26" height="14" viewBox="0 0 26 14"><path d="M8 2 L3 7 L8 12 M18 2 L23 7 L18 12" stroke="#444" stroke-width="2" fill="none"/></svg>
<div class="abs quote-box">
  <svg class="abs" style="left:10px;top:6px" width="26" height="20" viewBox="0 0 26 20"><path d="M2 20 V10 Q2 2 10 0 V4 Q6 6 6 10 H11 V20Z M15 20 V10 Q15 2 23 0 V4 Q19 6 19 10 H24 V20Z" fill="#c9c9c9"/></svg>
  <p>Lorem ipsum dolor sit amet, consectetuer adipiscing elit. set diem nonumy nibh euis mod tincidunt ut laoreet dolor magna aliquam erat volutpat.</p>
  <span>Client Name, City</span>
  <svg class="abs" style="right:12px;top:26px" width="26" height="20" viewBox="0 0 26 20"><path d="M24 0 V10 Q24 18 16 20 V16 Q20 14 20 10 H15 V0Z M11 0 V10 Q11 18 3 20 V16 Q7 14 7 10 H2 V0Z" fill="#c9c9c9"/></svg>
</div>

<div class="abs qc">
  <div class="qc-head"><b>Quick Contact</b></div>
  <label style="top:57px">Name</label><div class="field" style="top:52px"></div>
  <label style="top:86px">Email</label><div class="field" style="top:81px"></div>
  <label style="top:115px">Phone</label><div class="field" style="top:110px"></div>
  <label style="top:144px">Message</label><div class="field" style="top:141px;height:82px"></div>
  <div class="btn qc-btn">SUBMIT</div>
</div>

<footer class="abs footer">
  <div class="footer-links">Home &nbsp;|&nbsp; About Us &nbsp;|&nbsp; Associates &nbsp;|&nbsp; Services &nbsp;|&nbsp; Our Mission &nbsp;|&nbsp; Investment Advice &nbsp;|&nbsp; General Financial Planning &nbsp;|&nbsp; Retirement Planning &nbsp;|&nbsp; 401K Planning &nbsp;|&nbsp; Latest News &nbsp;|&nbsp; Blogs &nbsp;|&nbsp; Contact</div>
  <div class="follow">Follow Us on : &nbsp;<i></i><i></i><i></i><i></i></div>
  <div class="copy">Copyright © 2013. Velmorfield.com. All rights reserved.</div>
</footer>
</body>
</html>
```